Corvale Spine & Joint Business Card

Need a business card using the logo provided. I want brand side of the card to be grey with the logo in the center of the card in white.

On the other side I leave to the designers

Target Market(s)

Personal Injury Attorneys

Industry/Entity Type

Medical

Contact Information for Business Card

Name, CEO. Cell Phone, (Ashford, Address, Phone) (Millbrook, Address, Phone) (Eastwater, Address, Phone)

Colors

Designer to choose only greyscale colors for use in the design.

Requirements
Must have
• Logo by itself on one side

```html
<!DOCTYPE html>
<html lang="en">
<head>
<meta charset="utf-8">
<title>Corvale Spine &amp; Joint — Business Card</title>
<link rel="stylesheet" href="https://fonts.googleapis.com/css2?family=Lato:wght@400;700&family=Karla:wght@400;700&display=swap">
<style>
  :root {
    --backdrop: #2b2d30;
    --card: #8fabb3;
    --logo-white: #ffffff;
    --accent-blue: #3573b5;
    --body-ink: #3c4b50;
    --spine-light: #f4f6f7;
    --spine-soft: #e3eaec;
  }
  * { box-sizing: border-box; margin: 0; padding: 0; }
  html, body {
    width: 1200px; height: 874px; overflow: hidden;
    background: var(--backdrop);
  }
  .canvas { position: relative; width: 1200px; height: 874px; }
  .card {
    position: absolute; left: 280px;
    width: 640px; height: 366px;
    background: var(--card);
    border-radius: 22px;
    overflow: hidden;
  }
  .card--front { top: 40px; }
  .card--back { top: 468px; }

  .brand {
    position: absolute; inset: 0;
    display: flex; flex-direction: column; align-items: center; justify-content: center;
    color: var(--logo-white);
    font-family: "Lato", sans-serif; font-weight: 700;
  }
  .brand__name { font-size: 62px; letter-spacing: 14px; line-height: 1; margin-right: -14px; }
  .brand__tag { font-size: 26px; letter-spacing: 8px; margin-top: 12px; margin-right: -8px; }

  .locations {
    position: absolute; left: 44px; top: 44px;
    font-family: "Karla", sans-serif; color: var(--body-ink);
    font-size: 15px; line-height: 19px;
  }
  .location + .location { margin-top: 10px; }
  .location__city { color: var(--accent-blue); font-weight: 700; }
  .location__phone { display: flex; align-items: center; gap: 6px; }
  .icon-phone { width: 11px; height: 11px; fill: var(--accent-blue); }

  .person {
    position: absolute; right: 196px; top: 150px;
    text-align: right;
    font-family: "Karla", sans-serif; color: var(--body-ink);
    font-size: 15px; line-height: 19px;
  }
  .person__name {
    color: var(--accent-blue); font-weight: 700;
    font-size: 19px; letter-spacing: 1px; line-height: 24px;
  }
  .person__title { color: var(--accent-blue); }
  .person__cell { display: flex; align-items: center; justify-content: flex-end; gap: 6px; }
  .icon-mobile { width: 9px; height: 15px; }

  .spine-art {
    position: absolute; right: 28px; top: 18px;
    width: 120px; height: 330px;
    border-radius: 14px 14px 40px 14px;
    background: linear-gradient(180deg, var(--spine-light), var(--spine-soft));
  }
</style>
</head>
<body>
<main class="canvas">

  <section class="card card--front" aria-label="Card front">
    <div class="brand">
      <span class="brand__name">CORVALE</span>
      <span class="brand__tag">SPINE &amp; JOINT</span>
    </div>
  </section>

  <section class="card card--back" aria-label="Card back">
    <div class="locations">
      <div class="location">
        <div class="location__city">Ashford</div>
        <div>4120 Larkspur Lane</div>
        <div>Brookfield, Oregon 97512</div>
        <div class="location__phone">
          <svg class="icon-phone" viewBox="0 0 24 24" aria-hidden="true"><path d="M6.6 10.8a15.1 15.1 0 0 0 6.6 6.6l2.2-2.2a1 1 0 0 1 1-.25 11.4 11.4 0 0 0 3.6.57 1 1 0 0 1 1 1V20a1 1 0 0 1-1 1A17 17 0 0 1 3 4a1 1 0 0 1 1-1h3.5a1 1 0 0 1 1 1c0 1.25.2 2.45.57 3.6a1 1 0 0 1-.25 1z"/></svg>
          <span>555-014-2783</span>
        </div>
      </div>
      <div class="location">
        <div class="location__city">Millbrook</div>
        <div>4120 Larkspur Lane</div>
        <div>Brookfield, Oregon 97512</div>
        <div class="location__phone">
          <svg class="icon-phone" viewBox="0 0 24 24" aria-hidden="true"><path d="M6.6 10.8a15.1 15.1 0 0 0 6.6 6.6l2.2-2.2a1 1 0 0 1 1-.25 11.4 11.4 0 0 0 3.6.57 1 1 0 0 1 1 1V20a1 1 0 0 1-1 1A17 17 0 0 1 3 4a1 1 0 0 1 1-1h3.5a1 1 0 0 1 1 1c0 1.25.2 2.45.57 3.6a1 1 0 0 1-.25 1z"/></svg>
          <span>555-014-2783</span>
        </div>
      </div>
      <div class="location">
        <div class="location__city">Eastwater</div>
        <div>4120 Larkspur Lane</div>
        <div>Brookfield, Oregon 97512</div>
        <div class="location__phone">
          <svg class="icon-phone" viewBox="0 0 24 24" aria-hidden="true"><path d="M6.6 10.8a15.1 15.1 0 0 0 6.6 6.6l2.2-2.2a1 1 0 0 1 1-.25 11.4 11.4 0 0 0 3.6.57 1 1 0 0 1 1 1V20a1 1 0 0 1-1 1A17 17 0 0 1 3 4a1 1 0 0 1 1-1h3.5a1 1 0 0 1 1 1c0 1.25.2 2.45.57 3.6a1 1 0 0 1-.25 1z"/></svg>
          <span>555-014-2783</span>
        </div>
      </div>
    </div>

    <div class="person">
      <div class="person__name">DANIEL REYES</div>
      <div class="person__title">President</div>
      <div class="person__cell">
        <span>555-014-2783</span>
        <svg class="icon-mobile" viewBox="0 0 9 15" aria-hidden="true"><rect x="0.75" y="0.75" width="7.5" height="13.5" rx="1.5" fill="none" stroke="var(--accent-blue)" stroke-width="1.5"/><line x1="3" y1="12" x2="6" y2="12" stroke="var(--accent-blue)" stroke-width="1.2"/></svg>
      </div>
    </div>

    <div class="spine-art" role="img" aria-label="White illustration of a column of spinal vertebrae running down the right edge"></div>
  </section>

</main>
</body>
</html>
```